Stationery Design + Business Cards

Stationary (letterhead as A4 210x297mm and Letter 8.5"x11", preferably both master page + 2nd pages)

Also need business cards, standard size 50x88mm, can be vertical or horizontal.

You can use a front/back design for the business cards, or front only.

Looking at the uploaded file (dolvek, you already have that), I want it to use the first logo on the list (4 colors).

Alternative, try the grayscale version (second file).

I need the following information on the business card (in no particular order, let me know what you come up with): 

Firstname Lastlame 
Title 

Mobile +1 317-555-0147 

Velmarix, Inc. 
24819 Birchwood Ridge Pass 
Carmel, IN 46195 
Tel. +1 317-555-0182 
Fax +1 317-555-0163 

Web: www.velmarix.com 
Twitter: twitter/Velmarix or @Velmarix 
Facebook: facebook.com/Velmarix 

For letterhead, just the company name, address + phone number & fax number 

If you think the phone/fax or something else should not be on the business cards, or something could be missing, let me know.

```html
<!DOCTYPE html>
<html lang="en">
<head>
<meta charset="utf-8">
<title>Velmarix Letterhead</title>
<link rel="stylesheet" href="https://fonts.googleapis.com/css2?family=Source+Sans+3:wght@400&display=swap">
<style>
  :root {
    --canvas: #ffffff;
    --paper: #ffffff;
    --paper-edge: #d6d6d6;
    --ink: #58595b;
    --mark: #6a6a6a;
    --band: #6d6e70;
    --band-text: #ffffff;
  }
  * { margin: 0; padding: 0; box-sizing: border-box; }
  html, body {
    width: 1200px;
    height: 960px;
    overflow: hidden;
    background: var(--canvas);
    font-family: "Source Sans 3", "Myriad Pro", Arial, sans-serif;
  }
  .letterhead {
    position: absolute;
    left: 278px;
    top: 25px;
    width: 644px;
    height: 911px;
    background: var(--paper);
    border: 1px solid var(--paper-edge);
    box-shadow: 0 1px 4px rgba(0, 0, 0, 0.18);
  }
  .brand {
    position: absolute;
    display: flex;
    align-items: center;
    color: var(--ink);
    font-weight: 400;
    white-space: nowrap;
  }
  .brand-dot {
    border-radius: 50%;
    background: var(--mark);
    flex: none;
  }
  .brand--header {
    left: 247px;
    top: 62px;
    font-size: 27px;
    gap: 9px;
  }
  .brand--header .brand-dot { width: 32px; height: 32px; }
  .footer-band {
    position: absolute;
    left: 43px;
    top: 847px;
    width: 490px;
    height: 31px;
    background: var(--band);
    color: var(--band-text);
    font-size: 8.6px;
    line-height: 31px;
    padding-left: 10px;
    white-space: nowrap;
    letter-spacing: 0.05px;
  }
  .footer-band .sep { margin: 0 3px; }
  .brand--footer {
    left: 519px;
    top: 851px;
    font-size: 15px;
    gap: 5px;
  }
  .brand--footer .brand-dot { width: 18px; height: 18px; }
</style>
</head>
<body>
  <main class="letterhead">
    <header class="brand brand--header">
      <span class="brand-dot"></span>
      <span class="brand-name">Velmarix</span>
    </header>

    <footer>
      <div class="footer-band">
        Velmarix, Inc.<span class="sep">|</span>24819 Birchwood Ridge Pass<span class="sep">|</span>Carmel, IN 46195<span class="sep">|</span>Tel. +1 317-555-0182<span class="sep">|</span>Fax +1 317-555-0163
      </div>
      <div class="brand brand--footer">
        <span class="brand-dot"></span>
        <span class="brand-name">Velmarix</span>
      </div>
    </footer>
  </main>
</body>
</html>
```